Creative, Colorful, Dynamic Infographic for Global Non-Profit

We are a global arts and education non-profit in need of an infographic that illustrates four key skills embedded in our work: Curiosity, Listening, Imagination, Postive Action.
We work primarily with educators, students, and artists who use the power of personal stories to build community and connection and to bridge divides.
Our new brand guidelines, logos, and fonts are here: https://stylekit.example/lanternfold-9
I've attached a mock-up of the graphic and the required text. (Note the attached design was created by a staff person, your final design does not need to be the same. The color scheme and text of the final design should match the brand guidelines above.)
The graphic will be used for both web and print media and should include the purple Lanternfold 9 logo (also attached).
Ideally the final design will delight audiences and spark interest in our work.

```html
<!DOCTYPE html>
<html lang="en">
<head>
<meta charset="utf-8">
<title>Lanternfold 9 — Four Skills</title>
<link rel="stylesheet" href="https://fonts.googleapis.com/css2?family=Libre+Franklin:wght@400;500&family=Source+Serif+4:wght@700&display=swap">
<style>
  :root {
    --paper: #ffffff;
    --ink-dark: #1f1d3d;
    --curiosity: #6a3299;
    --curiosity-band: #9b7bc2;
    --action: #e8c94a;
    --action-band: #f3e29e;
    --imagination: #ee4545;
    --imagination-band: #f59c99;
    --listening: #2267c2;
    --listening-band: #84a8dd;
    --on-colour: #ffffff;
    --band-text: #2a2440;
  }
  html, body {
    margin: 0;
    padding: 0;
    width: 1200px;
    height: 767px;
    overflow: hidden;
    background: var(--paper);
  }
  .skills-board {
    display: block;
    width: 1200px;
    height: 767px;
  }
  .skill-title {
    font-family: "Source Serif 4", Georgia, serif;
    font-weight: 700;
    font-size: 15px;
    fill: var(--on-colour);
    text-anchor: middle;
  }
  .skill-copy {
    font-family: "Libre Franklin", Arial, sans-serif;
    font-size: 8.6px;
    fill: var(--on-colour);
    text-anchor: middle;
  }
  .link-copy {
    font-family: "Libre Franklin", Arial, sans-serif;
    font-weight: 500;
    font-size: 7.2px;
    fill: var(--band-text);
    text-anchor: middle;
  }
  .brand-name {
    font-family: "Source Serif 4", Georgia, serif;
    font-weight: 700;
    fill: var(--on-colour);
    text-anchor: middle;
  }
  .node-curiosity { fill: var(--curiosity); }
  .node-action { fill: var(--action); }
  .node-imagination { fill: var(--imagination); }
  .node-listening { fill: var(--listening); }
  .band-curiosity { fill: var(--curiosity-band); }
  .band-action { fill: var(--action-band); }
  .band-imagination { fill: var(--imagination-band); }
  .band-listening { fill: var(--listening-band); }
  .ring-arc { fill: none; stroke-width: 50; }
  .ring-action { stroke: var(--action-band); }
  .ring-imagination { stroke: var(--imagination-band); }
  .ring-listening { stroke: var(--listening-band); }
  .ring-curiosity { stroke: var(--curiosity-band); }
  .hub-clear { fill: var(--paper); }
  .hub-mark { fill: var(--ink-dark); }
  .flow-arrow { fill: var(--paper); }
</style>
</head>
<body>
<svg class="skills-board" viewBox="0 0 930 594.4" preserveAspectRatio="xMidYMid meet" role="img" aria-label="Four skills of Lanternfold 9: Curiosity, Listening, Imagination and Positive action, shown as two connected cycles">

  <!-- Cluster layout -->
  <g class="skills-cluster">
    <path class="band-action" d="M130,100 Q250,145 368,100 L368,200 L130,200 Z"/>
    <path class="band-curiosity" d="M70,190 Q108,290 70,390 L180,390 L180,190 Z"/>
    <path class="band-imagination" d="M430,190 Q392,290 430,390 L320,390 L320,190 Z"/>
    <path class="band-listening" d="M130,470 Q250,430 368,470 L368,380 L130,380 Z"/>

    <circle class="hub-clear" cx="249" cy="290" r="128"/>
    <circle class="hub-mark" cx="249" cy="290" r="67"/>
    <text class="brand-name" x="249" y="295" font-size="13">Lanternfold 9</text>

    <text class="link-copy" x="249" y="148">Your positive actions lead</text>
    <text class="link-copy" x="249" y="157">to curiosity about what else is possible</text>

    <text class="link-copy" transform="translate(113,290) rotate(-90)">Your curiosity allows you to listen</text>

    <g transform="translate(382,290) rotate(90)">
      <text class="link-copy" x="0" y="-3">Your imagination</text>
      <text class="link-copy" x="0" y="6">can spark positive action</text>
    </g>

    <text class="link-copy" x="249" y="428">Your listening allows you to</text>
    <text class="link-copy" x="249" y="437">take in new information</text>

    <g class="skill-node">
      <circle class="node-curiosity" cx="114" cy="155" r="68"/>
      <text class="skill-title" x="114" y="138">Curiosity</text>
      <text class="skill-copy" x="114" y="157">Focus on how you</text>
      <text class="skill-copy" x="114" y="168">can learn from</text>
      <text class="skill-copy" x="114" y="179">another's knowledge</text>
      <text class="skill-copy" x="114" y="190">and experience</text>
    </g>
    <g class="skill-node">
      <circle class="node-action" cx="383" cy="155" r="68"/>
      <text class="skill-title" x="383" y="155">Positive action</text>
      <text class="skill-copy" x="383" y="172">Show your words</text>
      <text class="skill-copy" x="383" y="183">and actions matter</text>
    </g>
    <g class="skill-node">
      <circle class="node-listening" cx="114" cy="426" r="68"/>
      <text class="skill-title" x="114" y="417">Listening</text>
      <text class="skill-copy" x="114" y="438">Seek to understand</text>
      <text class="skill-copy" x="114" y="449">before speaking</text>
    </g>
    <g class="skill-node">
      <circle class="node-imagination" cx="383" cy="426" r="68"/>
      <text class="skill-title" x="383" y="413">Imagination</text>
      <text class="skill-copy" x="383" y="438">Consider possibilities</text>
      <text class="skill-copy" x="383" y="449">beyond what you know</text>
    </g>
  </g>

  <!-- Ring layout -->
  <g class="skills-ring">
    <path class="ring-arc ring-action" d="M551.7,167.7 A173,173 0 0 1 796.3,167.7"/>
    <path class="ring-arc ring-imagination" d="M796.3,167.7 A173,173 0 0 1 796.3,412.3"/>
    <path class="ring-arc ring-listening" d="M796.3,412.3 A173,173 0 0 1 551.7,412.3"/>
    <path class="ring-arc ring-curiosity" d="M551.7,412.3 A173,173 0 0 1 551.7,167.7"/>

    <circle class="hub-mark" cx="674" cy="290" r="50"/>
    <text class="brand-name" x="674" y="294" font-size="10">Lanternfold 9</text>

    <polygon class="flow-arrow" points="631,132 638,127.5 638,136.5"/>
    <text class="link-copy" x="682" y="120">Your positive</text>
    <text class="link-copy" x="682" y="129">actions lead to</text>
    <text class="link-copy" x="682" y="138">curiosity about what</text>
    <text class="link-copy" x="682" y="147">else is possible</text>

    <polygon class="flow-arrow" points="831,248 826.5,255 835.5,255"/>
    <text class="link-copy" x="831" y="277">Your</text>
    <text class="link-copy" x="831" y="286">imagination</text>
    <text class="link-copy" x="831" y="295">can spark</text>
    <text class="link-copy" x="831" y="304">positive action</text>

    <text class="link-copy" x="516" y="283">Your curiosity</text>
    <text class="link-copy" x="516" y="292">allows you to</text>
    <text class="link-copy" x="516" y="301">listen</text>
    <polygon class="flow-arrow" points="516,331 511.5,324 520.5,324"/>

    <text class="link-copy" x="668" y="445">Your listening</text>
    <text class="link-copy" x="668" y="454">allows you to take</text>
    <text class="link-copy" x="668" y="463">in new information</text>
    <polygon class="flow-arrow" points="718,452 711,447.5 711,456.5"/>

    <g class="skill-node">
      <circle class="node-curiosity" cx="555" cy="172" r="68"/>
      <text class="skill-title" x="555" y="155">Curiosity</text>
      <text class="skill-copy" x="555" y="175">Focus on how you</text>
      <text class="skill-copy" x="555" y="186">can learn from</text>
      <text class="skill-copy" x="555" y="197">another's knowledge</text>
      <text class="skill-copy" x="555" y="208">and experience</text>
    </g>
    <g class="skill-node">
      <circle class="node-action" cx="792" cy="172" r="68"/>
      <text class="skill-title" x="792" y="171">Positive action</text>
      <text class="skill-copy" x="792" y="188">Show your words</text>
      <text class="skill-copy" x="792" y="199">and actions matter</text>
    </g>
    <g class="skill-node">
      <circle class="node-listening" cx="555" cy="410" r="68"/>
      <text class="skill-title" x="555" y="401">Listening</text>
      <text class="skill-copy" x="555" y="422">Seek to understand</text>
      <text class="skill-copy" x="555" y="433">before speaking</text>
    </g>
    <g class="skill-node">
      <circle class="node-imagination" cx="792" cy="410" r="68"/>
      <text class="skill-title" x="792" y="398">Imagination</text>
      <text class="skill-copy" x="792" y="422">Consider possibilities</text>
      <text class="skill-copy" x="792" y="433">beyond what you know</text>
    </g>
  </g>
</svg>
</body>
</html>
```